Quorvix Letter head

Quorvix is a young and energetic software development consultancy. We spend our time working with clients to turn what ever is in their heads in to software.
We are trying to create an image of a high class software boutique who build class leading bespoke solutions.
We need a sharp letter head that looks great on high quality media.
We like bold colours and distinctive design. So show us what you can do.
Industry/Entity Type
Software
Requirements
Must have
- Our company is based in the UK and are requried to have on the paper somewhere the following information:
* Registered company name: Quorvix Ltd
* Registered company number
* VAT registration number
In addition we also want the following:
* An email address
* Telephone number
* Website address
An example of what some pages have in their footer is something like the following:
Quorvix Ltd is registered in England and Wales. Reg. no: 5316274
Registered office: 48 Cobblewick Road, Harlow Essex, CM93TP. Tel: 07712365081
You do not have to use this sentance but please make sure your design incorporates accommodates the requirements for UK based companies

```html
<!DOCTYPE html>
<html lang="en">
<head>
<meta charset="utf-8">
<title>Quorvix Letterhead</title>
<link href="https://fonts.googleapis.com/css2?family=Jost:wght@400;500;700&display=swap" rel="stylesheet">
<style>
  :root {
    --brand-red: #d0132a;
    --ink: #2a2a2a;
    --muted: #6e6e6e;
    --rule-grey: #9a9a9a;
    --paper: #f7f7f7;
    --folder-light: #b9b9bb;
    --folder-dark: #8e8e90;
    --stage: #e6e4e1;
  }
  * { box-sizing: border-box; margin: 0; padding: 0; }
  html, body { width: 1200px; height: 720px; overflow: hidden; }
  body {
    background: var(--stage);
    font-family: "Jost", "Futura", sans-serif;
    color: var(--ink);
    position: relative;
  }

  /* Folder cover */
  .folder-cover {
    position: absolute;
    left: 110px; top: 30px;
    width: 470px; height: 660px;
    background: radial-gradient(ellipse at 50% 45%, var(--folder-light) 0%, var(--folder-dark) 100%);
    display: flex; flex-direction: column; align-items: center; justify-content: center;
    box-shadow: 0 4px 18px rgba(0,0,0,.18);
  }
  .folder-cover .wordmark { font-size: 30px; }
  .folder-cover .web-address {
    margin-top: 6px; font-size: 11px; color: #e9e9e9; letter-spacing: .5px;
  }

  .wordmark {
    font-weight: 500;
    color: var(--brand-red);
    letter-spacing: 1px;
    text-transform: uppercase;
    line-height: 1;
  }

  /* Letterhead sheet */
  .letterhead {
    position: absolute;
    left: 620px; top: 30px;
    width: 470px; height: 660px;
    background: var(--paper);
    box-shadow: 0 4px 18px rgba(0,0,0,.2);
    overflow: hidden;
  }
  .letterhead-header {
    position: absolute; left: 28px; right: 26px; top: 34px;
    display: flex; justify-content: space-between; align-items: flex-start;
  }
  .letterhead-header .wordmark { font-size: 22px; }
  .company-details { display: flex; gap: 12px; font-size: 6px; line-height: 1.45; color: var(--muted); margin-top: 38px; }
  .company-details strong { color: var(--ink); font-weight: 700; }
  .contact-list { list-style: none; }
  .contact-list li { display: flex; align-items: center; gap: 4px; }
  .contact-list svg { width: 6px; height: 6px; fill: var(--brand-red); }

  .letter-body {
    position: absolute; left: 52px; right: 40px; top: 118px;
    font-size: 8px; line-height: 1.42;
  }
  .recipient { margin-bottom: 22px; }
  .recipient strong { font-weight: 700; }
  .letter-body p { text-align: justify; margin-bottom: 10px; }
  .sign-off { margin-top: 22px; }
  .sign-off strong { font-weight: 700; display: block; }

  .letterhead-footer { position: absolute; left: 0; bottom: 0; width: 470px; height: 110px; }
  .footer-legal {
    position: absolute; left: 30px; bottom: 66px;
    font-size: 5.5px; color: var(--muted); letter-spacing: .2px;
  }
</style>
</head>
<body>

  <section class="folder-cover">
    <div class="wordmark">Quorvix</div>
    <div class="web-address">www.quorvix.com</div>
  </section>

  <article class="letterhead">
    <header class="letterhead-header">
      <div class="wordmark">Quorvix</div>
      <div class="company-details">
        <address style="font-style:normal">
          <strong>Quorvix Ltd.</strong><br>
          48 Cobblewick Road<br>
          Harlow Essex, CM93TP
        </address>
        <ul class="contact-list">
          <li><svg viewBox="0 0 10 10"><path d="M2 1h2l1 2-1 1a5 5 0 0 0 2 2l1-1 2 1v2c-4 1-8-3-7-7z"/></svg>07712365081</li>
          <li><svg viewBox="0 0 10 10"><rect x="1" y="2" width="8" height="6"/></svg>01279 450 118</li>
          <li><svg viewBox="0 0 10 10"><circle cx="5" cy="5" r="4"/></svg>info@quorvix.com</li>
        </ul>
      </div>
    </header>

    <div class="letter-body">
      <address class="recipient" style="font-style:normal">
        <strong>Mr. Daniel Hart</strong><br>
        Managing Director<br>
        USA Investor<br>
        12 Ashgrove Lane
      </address>
      <p>Lorem Ipsum is simply dummy text for printing and typesetting industry. Lorem Ipsum has been the industry's standard dummy text since the 1500s, when an unknown printer galley of type and scrambled it to make a type specimen book. It has survived not only manual but also the leap into electronic typesetting, remaining essentially un changed. It was popularised in the 1960s with the release of Transfix sheets containing Lorem Ipsum pass and more recently with desktop publishing software like Setwell Composer including version 6.9 of Lorem Ipsum.</p>
      <p>Country to popular belief, Lorem Ipsum is not simply random text. It has roots in a piece of sical Latin literature from 45 BC, making it over 2000 years old. Edmund Halloway, a prfessor at Ashbury-Lyle College in discovered the undoubtable sorce. Lorem Ipsum comes from section 1.10.32 and 1.10.33 of "de Finibus Bonorum et Molorum" (The Extreme of Good and Even Marcus Tullian), written in 45 BC. This book is a treatise on the theory of ethics very popular during Renassiance.</p>
      <p>Thank you for being one of our valued customers.</p>
      <div class="sign-off"><strong>Name Here</strong>CEO</div>
    </div>

    <p class="footer-legal">Reg. No.: 5316274 Registered in England &nbsp;&nbsp; VAT Reg No.: GB 482 7156 03</p>
    <svg class="letterhead-footer" viewBox="0 0 470 110" preserveAspectRatio="none" aria-hidden="true">
      <path d="M0 52 L400 72 Q430 74 440 60 L470 60" fill="none" stroke="var(--rule-grey)" stroke-width="1.5"/>
      <path d="M0 58 L400 80 Q432 82 444 66 L470 66" fill="none" stroke="var(--rule-grey)" stroke-width="1"/>
      <path d="M0 64 L470 92 L470 110 L0 110 Z" fill="var(--brand-red)"/>
      <path d="M0 64 L470 92" fill="none" stroke="#ffffff" stroke-width="1.2"/>
    </svg>
  </article>

</body>
</html>
```